eBook cover and content: Steering Teams Beyond the Obvious Path

I teach a leadership program to companies that was developed at Vantrel and now need an eBook cover and content design. This downloadable eBook will be offered online in exchange for prospects' contact details. It needs to be designed with a sophisticated, senior HR executive audience in mind. There are some assets that are available for you to work with including photographs, a logo device for the program, and a colour palette (same as Vantrel's blue, green, yellow and red). Note that while the program was developed at Vantrel it is NOT a Vantrel product and I need to ensure that the eBook does not breach license guidelines. I have attached a very rough mockup of the content, images and graphic elements to help.

Target Market(s)

Senior business leaders and HR professionals.

Industry/Entity Type

Leadership

Font styles to use
Sans Serif

Requirements
Must have
• Keep it simple. Clean, contemporary, professional feel. This is a high-value decision for a company and needs to look modern, progressive and credible. Downloadable PDF. Easy to read and digest layout.
• Colours - see attached screenshot for red, blue, green, yellow ref. Additionally charcoal for most type and purple 330033 as extra colour is okay.
• Landscape format please.
Nice to have
• Plenty of white space.

```html
<!DOCTYPE html>
<html lang="en">
<head>
<meta charset="utf-8">
<title>Steering Teams Beyond the Obvious Path — eBook Cover</title>
<link rel="stylesheet" href="https://fonts.googleapis.com/css2?family=Oswald:wght@300;500&display=swap">
<style>
  :root {
    --paper: #ffffff;
    --trim: #6d6e71;
    --glow: #f6b531;
    --glow-soft: #fde7b8;
    --bulb-red: #e31e32;
    --charcoal: #231f20;
    --blue: #4f7fc4;
    --green: #1e9b4f;
    --yellow: #f6be1a;
    --red: #dd4a33;
  }
  * { margin: 0; padding: 0; box-sizing: border-box; }
  html, body {
    width: 1200px; height: 934px; overflow: hidden; background: var(--paper);
  }
  .cover {
    position: relative; width: 1200px; height: 934px; background: var(--paper);
    font-family: "Oswald", "Arial Narrow", sans-serif;
  }
  .print-marks {
    position: absolute; inset: 0; width: 1200px; height: 934px;
  }
  .bulb-illustration {
    position: absolute; left: 440px; top: 208px; width: 294px; height: 378px;
    border-radius: 50% 50% 40% 40% / 42% 42% 58% 58%;
    background: radial-gradient(ellipse 55% 48% at 50% 40%,
      var(--glow) 0%, var(--glow-soft) 55%, rgba(255,255,255,0) 100%);
  }
  .title {
    position: absolute; left: 487px; top: 240px; width: 200px;
    color: var(--charcoal); text-align: center; font-weight: 300;
    line-height: 1.05;
  }
  .title span { display: block; }
  .title .lead { font-size: 36px; letter-spacing: 0.5px; }
  .title .key { font-size: 64px; font-weight: 500; line-height: 1; margin: 2px 0 4px; }
  .title .sub { font-size: 28px; }
  .team-figures {
    position: absolute; left: 401px; top: 600px; width: 382px; height: 121px;
    background: linear-gradient(90deg,
      var(--green) 0%, var(--blue) 12%, var(--red) 24%, var(--red) 40%,
      var(--green) 44%, var(--yellow) 50%, var(--red) 56%, var(--blue) 68%,
      var(--green) 80%, var(--blue) 92%);
    opacity: 0.8;
  }
  .author {
    position: absolute; left: 0; width: 1200px; top: 778px;
    text-align: center; font-size: 40px; font-weight: 300;
    color: var(--charcoal); letter-spacing: 1px;
  }
  .program-mark {
    position: absolute; left: 114px; top: 794px;
    display: flex; align-items: center; gap: 6px;
    font-size: 20px; font-weight: 500; color: var(--blue);
  }
  .program-mark .dot {
    width: 12px; height: 12px; border-radius: 50%; background: var(--blue);
  }
</style>
</head>
<body>
<div class="cover">
  <svg class="print-marks" viewBox="0 0 1200 934" aria-hidden="true">
    <rect x="73.5" y="69.5" width="1060" height="795" fill="none" stroke="var(--trim)" stroke-width="1"/>
    <g stroke="var(--trim)" stroke-width="1">
      <line x1="73.5" y1="12" x2="73.5" y2="50"/>
      <line x1="1133.5" y1="12" x2="1133.5" y2="50"/>
      <line x1="73.5" y1="884" x2="73.5" y2="922"/>
      <line x1="1133.5" y1="884" x2="1133.5" y2="922"/>
      <line x1="16" y1="69.5" x2="54" y2="69.5"/>
      <line x1="1152" y1="69.5" x2="1190" y2="69.5"/>
      <line x1="16" y1="864.5" x2="54" y2="864.5"/>
      <line x1="1152" y1="864.5" x2="1190" y2="864.5"/>
    </g>
  </svg>

  <div class="bulb-illustration" role="img" aria-label="Glowing red outline lightbulb illustration with rays, holding the title"></div>

  <h1 class="title">
    <span class="lead">Steering</span>
    <span class="key">Teams</span>
    <span class="sub">Beyond the</span>
    <span class="sub">Obvious Path</span>
  </h1>

  <div class="team-figures" role="img" aria-label="Row of colourful silhouettes of business people standing together in blue, green, red and yellow"></div>

  <p class="author">Colin Dane</p>

  <p class="program-mark"><span class="dot"></span>Keystep</p>
</div>
</body>
</html>
```